Bellwood Tax
Project: Business Cards and Stationery
Business Cards and Stationery - Consulting
Business Cards and Stationery
Modern
Peter Marsh
President
28617 Coralind Ave., 4th Floor Larkmont, WE 90572
peterm@bellwdtax.example
www.bellwoodtaxservice.example

```html
<!DOCTYPE html>
<html lang="en">
<head>
<meta charset="utf-8">
<title>Bellwood Tax – Business Cards and Stationery</title>
<link href="https://fonts.googleapis.com/css2?family=Tinos&family=Arimo:wght@400;700&display=swap" rel="stylesheet">
<style>
  :root{
    --stage:#000;
    --paper:#ffffff;
    --paper-shade:#d9dadc;
    --blue:#1e9ad8;
    --blue-deep:#0a62b5;
    --ink:#16243f;
    --brand:#1f2d44;
  }
  *{margin:0;padding:0;box-sizing:border-box}
  html,body{width:1200px;height:871px;overflow:hidden;background:var(--stage)}
  .stage{position:relative;width:1200px;height:871px}
  .piece{position:absolute;overflow:hidden}
  .piece svg.shape{position:absolute;inset:0;width:100%;height:100%}

  .brand{display:flex;align-items:center;gap:10px;font-family:"Tinos",serif;color:var(--brand);text-transform:uppercase;white-space:nowrap}
  .brand .dot{border-radius:50%;background:var(--blue);flex:none}

  .contact{position:absolute;list-style:none;font-family:"Tinos",serif;color:var(--blue)}
  .contact li{display:flex;align-items:center;white-space:nowrap}
  .contact svg{flex:none;fill:var(--blue)}

  .person{font-family:"Arimo",sans-serif;text-align:center}

  /* letterhead left */
  .letter-a{left:60px;top:29px;width:408px;height:542px;background:linear-gradient(100deg,var(--paper) 35%,var(--paper-shade) 100%)}
  .letter-a .contact{left:26px;top:16px;font-size:10px;line-height:1.2}
  .letter-a .contact li{gap:10px;margin-bottom:9px}
  .letter-a .contact svg{width:12px;height:12px}
  .letter-a .brand{position:absolute;left:20px;top:464px;font-size:28px}
  .letter-a .brand .dot{width:34px;height:34px}
  .letter-a .person{position:absolute;left:60px;top:505px;width:150px;color:var(--blue);font-size:15px;line-height:1.1}

  /* letterhead right */
  .letter-b{left:737px;top:29px;width:408px;height:542px;background:linear-gradient(260deg,var(--paper) 30%,var(--paper-shade) 100%)}
  .letter-b .brand{position:absolute;right:22px;top:28px;font-size:27px}
  .letter-b .brand .dot{width:32px;height:32px}
  .letter-b .person{position:absolute;right:40px;top:62px;width:170px;color:var(--blue);font-size:15px;line-height:1.1}
  .letter-b .contact{left:100px;top:418px;font-size:10px}
  .letter-b .contact li{gap:10px;margin-bottom:9px}
  .letter-b .contact svg{width:12px;height:12px}

  /* small cards */
  .card-sm-front{left:526px;top:137px;width:125px;height:96px;background:linear-gradient(90deg,#f3f6f9 10%,var(--blue-deep) 100%)}
  .card-sm-front .brand{position:absolute;left:8px;top:22px;font-size:10.5px;gap:5px}
  .card-sm-front .brand .dot{width:14px;height:14px}
  .card-sm-front .person{position:absolute;left:0;top:50px;width:125px;color:var(--ink);font-size:10px;line-height:1.15}
  .card-sm-front .person .title{font-size:8px;font-weight:700}

  .card-sm-back{left:526px;top:283px;width:125px;height:101px;background:linear-gradient(90deg,#f7f8f9,#d7d9dc)}
  .card-sm-back .contact{left:26px;top:8px;font-size:5px;line-height:1.1}
  .card-sm-back .contact li{gap:5px;margin-bottom:5px}
  .card-sm-back .contact svg{width:6px;height:6px}

  /* large cards */
  .card-lg-front{left:60px;top:593px;width:408px;height:240px;background:linear-gradient(90deg,#f5f7fa 15%,#7fb1de 60%,var(--blue-deep) 100%)}
  .card-lg-front .brand{position:absolute;left:38px;top:58px;font-size:32px;gap:14px}
  .card-lg-front .brand .dot{width:40px;height:40px}
  .card-lg-front .person{position:absolute;left:0;top:134px;width:408px;color:var(--ink);font-size:23px;line-height:1.2}
  .card-lg-front .person .title{font-size:15px;font-weight:700}

  .card-lg-back{left:737px;top:593px;width:408px;height:240px;background:linear-gradient(90deg,#f5f7fa 20%,#8dbbe3 62%,var(--blue-deep) 100%)}
  .card-lg-back .brand{position:absolute;left:36px;top:58px;font-size:32px;gap:14px}
  .card-lg-back .brand .dot{width:40px;height:40px}
  .card-lg-back .web{position:absolute;left:0;top:155px;width:408px;text-align:center;font-family:"Tinos",serif;font-size:20px;color:#0b1426;white-space:nowrap}
</style>
</head>
<body>
<svg width="0" height="0" style="position:absolute" aria-hidden="true">
  <defs>
    <symbol id="ic-pin" viewBox="0 0 24 24"><path d="M12 2a7 7 0 0 0-7 7c0 5 7 13 7 13s7-8 7-13a7 7 0 0 0-7-7zm0 9.5A2.5 2.5 0 1 1 12 6.5a2.5 2.5 0 0 1 0 5z"/></symbol>
    <symbol id="ic-phone" viewBox="0 0 24 24"><path d="M6.6 10.8a15 15 0 0 0 6.6 6.6l2.2-2.2a1 1 0 0 1 1-.25 11.4 11.4 0 0 0 3.6.57 1 1 0 0 1 1 1V20a1 1 0 0 1-1 1A17 17 0 0 1 3 4a1 1 0 0 1 1-1h3.5a1 1 0 0 1 1 1c0 1.25.2 2.45.57 3.57a1 1 0 0 1-.25 1z"/></symbol>
    <symbol id="ic-fax" viewBox="0 0 24 24"><path d="M6 2h10v6H6zM3 9h18v9h-3v4H6v-4H3zm5 7v4h8v-4z"/></symbol>
    <symbol id="ic-mail" viewBox="0 0 24 24"><path d="M2 5h20v14H2zm2 2v.5l8 5 8-5V7z"/></symbol>
    <symbol id="ic-web" viewBox="0 0 24 24"><path d="M12 2a10 10 0 1 0 0 20 10 10 0 0 0 0-20zm0 2c.9 1.2 1.6 2.6 2 4h-4c.4-1.4 1.1-2.8 2-4zM4.3 14a8 8 0 0 1 0-4h3.4a16 16 0 0 0 0 4zm5.4 0a14 14 0 0 1 0-4h4.6a14 14 0 0 1 0 4zm6.6 0a16 16 0 0 0 0-4h3.4a8 8 0 0 1 0 4z"/></symbol>
  </defs>
</svg>

<main class="stage">

  <section class="piece letter-a">
    <svg class="shape" viewBox="0 0 408 542" preserveAspectRatio="none" aria-hidden="true">
      <path d="M288 0 L408 0 L408 542 C404 330 372 140 288 0 Z" fill="var(--blue)"/>
    </svg>
    <ul class="contact">
      <li><svg><use href="#ic-pin"/></svg><span>28617 Coralind Ave., 4th Floor<br>Larkmont, WE 90572</span></li>
      <li><svg><use href="#ic-phone"/></svg><span>800-555-0142</span></li>
      <li><svg><use href="#ic-fax"/></svg><span>800-555-0178</span></li>
      <li><svg><use href="#ic-mail"/></svg><span>peterm@bellwdtax.example</span></li>
      <li><svg><use href="#ic-web"/></svg><span>www.bellwoodtaxservice.example</span></li>
    </ul>
    <div class="brand"><span class="dot"></span>Bellwood Tax</div>
    <div class="person">Peter Marsh<br>President</div>
  </section>

  <section class="piece card-sm-front">
    <div class="brand"><span class="dot"></span>Bellwood Tax</div>
    <div class="person">Peter Marsh<br><span class="title">President</span></div>
  </section>

  <section class="piece card-sm-back">
    <svg class="shape" viewBox="0 0 125 101" preserveAspectRatio="none" aria-hidden="true">
      <path d="M0 0 L20 0 C14 35 14 70 22 101 L0 101 Z" fill="var(--blue)"/>
    </svg>
    <ul class="contact">
      <li><svg><use href="#ic-pin"/></svg><span>28617 Coralind Ave., 4th Floor<br>Larkmont, WE 90572</span></li>
      <li><svg><use href="#ic-phone"/></svg><span>800-555-0142</span></li>
      <li><svg><use href="#ic-fax"/></svg><span>800-555-0178</span></li>
      <li><svg><use href="#ic-mail"/></svg><span>peterm@bellwdtax.example</span></li>
      <li><svg><use href="#ic-web"/></svg><span>www.bellwoodtaxservice.example</span></li>
    </ul>
  </section>

  <section class="piece letter-b">
    <svg class="shape" viewBox="0 0 408 542" preserveAspectRatio="none" aria-hidden="true">
      <path d="M0 50 C50 190 84 380 78 542 L0 542 Z" fill="var(--blue)"/>
    </svg>
    <div class="brand"><span class="dot"></span>Bellwood Tax</div>
    <div class="person">Peter Marsh<br>President</div>
    <ul class="contact">
      <li><svg><use href="#ic-pin"/></svg><span>28617 Coralind Ave., 4th Floor<br>Larkmont, WE 90572</span></li>
      <li><svg><use href="#ic-phone"/></svg><span>800-555-0142</span></li>
      <li><svg><use href="#ic-fax"/></svg><span>800-555-0178</span></li>
      <li><svg><use href="#ic-mail"/></svg><span>peterm@bellwdtax.example</span></li>
      <li><svg><use href="#ic-web"/></svg><span>www.bellwoodtaxservice.example</span></li>
    </ul>
  </section>

  <section class="piece card-lg-front">
    <div class="brand"><span class="dot"></span>Bellwood Tax</div>
    <div class="person">Peter Marsh<br><span class="title">President</span></div>
  </section>

  <section class="piece card-lg-back">
    <div class="brand"><span class="dot"></span>Bellwood Tax</div>
    <div class="web">www.bellwoodtaxservice.example</div>
  </section>

</main>
</body>
</html>
```